Buch-/eBook-Cover für Sachbuch gesucht
Zielgruppe
We're selfpublishing nonfiction books. Interested are adults - mostly man (age range: 25-50) - who want to learn more about leadership at their workplaces.
Aufgabenstellung
The design should be clean and simple, title easy to read, good color contrast (the cover has to stand out from an white background).

```html
<!DOCTYPE html>
<html lang="en">
<head>
<meta charset="utf-8">
<title>Leadership – Book Cover</title>
<link rel="stylesheet" href="https://fonts.googleapis.com/css2?family=Bebas+Neue&family=Roboto:wght@300;400&display=swap">
<style>
  :root {
    --navy: #014174;
    --navy-deep: #013560;
    --cream: #f3efe7;
    --yellow: #ffcc00;
  }
  html, body {
    margin: 0;
    padding: 0;
    width: 750px;
    height: 1200px;
    overflow: hidden;
    background: #ffffff;
  }
  .cover {
    position: relative;
    width: 750px;
    height: 1200px;
    background: var(--navy);
    overflow: hidden;
  }
  .cover-art {
    position: absolute;
    inset: 0;
    width: 750px;
    height: 1200px;
  }
  .spotlight { fill: var(--yellow); }
  .walkers-area { fill: url(#walkersTone); }
  .author {
    font-family: "Roboto", sans-serif;
    font-weight: 400;
    font-size: 50px;
    fill: var(--cream);
  }
  .title {
    font-family: "Bebas Neue", "Oswald", sans-serif;
    font-size: 216px;
    fill: var(--cream);
  }
  .subtitle {
    font-family: "Roboto", sans-serif;
    font-weight: 300;
    font-size: 62px;
    letter-spacing: 1px;
    fill: var(--cream);
  }
</style>
</head>
<body>
  <main class="cover">
    <svg class="cover-art" viewBox="0 0 750 1200" xmlns="http://www.w3.org/2000/svg">
      <defs>
        <radialGradient id="walkersTone" cx="50%" cy="55%" r="60%">
          <stop offset="0%" stop-color="#0a2f52" stop-opacity="0.55"/>
          <stop offset="100%" stop-color="#014174" stop-opacity="0"/>
        </radialGradient>
      </defs>

      <polygon class="spotlight" points="476,707 750,332 750,796"/>

      <rect class="walkers-area" x="0" y="655" width="485" height="280"
            role="img" aria-label="Small silhouettes of business people walking toward the light, with long shadows"/>

      <text class="author" x="365" y="131" text-anchor="middle">Daniel Whitmore</text>

      <text class="title" x="53" y="333" textLength="510" lengthAdjust="spacingAndGlyphs">LEADER</text>
      <text class="title" x="50" y="520" textLength="262" lengthAdjust="spacingAndGlyphs">SHIP</text>

      <text class="subtitle" text-anchor="middle">
        <tspan x="373" y="1037">FOSTERING GROWTH</tspan>
        <tspan x="373" y="1104">AND INSPIRING</tspan>
        <tspan x="383" y="1171">EXCELLENCE</tspan>
      </text>
    </svg>
  </main>
</body>
</html>
```